Redo a PPT pres. - Real Estate in Brazil - Socially equitable investments in Social Housing

We need to redo the presentation attached. It is an institutional presentation to attract local and foreign investors to invest in Brazilian Social Housing Projects structured by our company "RTV".
A middle class of 100 million, a housing deficit of 9M, a strong political will & positive income generation trends constitute grounds for a significant demand in social housing.
This make a perfect scheme for investors to invest in Brazilian Social Housing.
"RTV", is a consulting "boutique" focused in Brazilian real estate, specialized in structuring, analyzing and originating Brazilian social housing projects.
RTV is part of the group RTK. RTK is structured to create value through each step of the residential real estate business - structuring, financing, sales, marketing and technology.
We would like to see designs that use mainly the color blue. The final design should communicate financial safety and professionalism. In order to reach our needs, the designer will need to have basic understanding of finance and investment in order to highlight the most important information.
The idea is to receive back the PPT with each page redesigned and an homogeneous identity.
To all designers,
Target Market(s)
Institutional Investors and wealthy individuals
Industry/Entity Type
Residential
Look and feel
Each slider illustrates characteristics of the customer's brand and the style your logo design should communicate.

```html
<!DOCTYPE html>
<html lang="en">
<head>
<meta charset="utf-8">
<title>Social Housing in Brazil – RTV</title>
<link href="https://fonts.googleapis.com/css2?family=Cinzel:wght@600;700&family=Libre+Baskerville:wght@700&family=Tinos:wght@700&family=Carlito:wght@400;700&display=swap" rel="stylesheet">
<style>
  :root {
    --stage: #d9d9d9;
    --navy: #14356e;
    --royal: #1f4f96;
    --deep: #0e2a5c;
    --band: #2d5596;
    --ink: #1b3263;
    --paper: #f1f2f5;
    --paper-edge: #dfe2e8;
    --node-top: #7fa6dc;
    --node-bot: #3f6fb5;
    --node-edge: #2a558f;
    --white: #ffffff;
    --silver: #c9ccd2;
  }
  * { box-sizing: border-box; margin: 0; padding: 0; }
  html, body { width: 955px; height: 1200px; overflow: hidden; }
  body {
    background: var(--stage);
    position: relative;
    font-family: "Tinos", "Times New Roman", serif;
  }
  .slide {
    position: absolute;
    width: 520px;
    height: 380px;
    overflow: hidden;
    box-shadow: 0 3px 10px rgba(0,0,0,.35);
  }
  .slide--cover { left: 25px; top: 15px;
    background: radial-gradient(ellipse at 40% 30%, var(--royal) 0%, var(--navy) 70%); }
  .slide--how { left: 415px; top: 410px; background: linear-gradient(var(--white), var(--paper) 60%, var(--paper-edge)); }
  .slide--agenda { left: 25px; top: 805px; background: linear-gradient(var(--white), var(--paper) 60%, var(--paper-edge)); }

  .brand {
    position: absolute; left: 12px; bottom: 8px;
    font-family: "Tinos", serif; font-weight: 700;
    font-size: 16px; color: var(--white);
    display: flex; align-items: center; gap: 5px;
  }
  .brand__dot { width: 8px; height: 8px; background: var(--white); }

  /* cover */
  .cover__title {
    position: absolute; left: 30px; top: 42px;
    font-family: "Cinzel", serif; font-weight: 700; white-space: nowrap;
    color: var(--white); font-size: 24px; letter-spacing: .5px;
    text-shadow: 1px 2px 3px rgba(0,0,0,.45);
  }
  .cover__rule {
    position: absolute; left: 25px; top: 80px; width: 440px; height: 3px;
    background: linear-gradient(90deg, transparent, var(--silver) 20%, var(--white) 60%, transparent);
  }
  .cover__subtitle {
    position: absolute; left: 95px; top: 96px; width: 340px;
    font-family: "Cinzel", serif; font-weight: 600;
    color: var(--white); font-size: 21px; line-height: 1.25; text-align: center;
    text-shadow: 1px 2px 3px rgba(0,0,0,.45);
  }
  .cover__map {
    position: absolute; left: 320px; top: 150px; width: 150px; height: 150px;
    border-radius: 45% 40% 50% 35%;
    background: radial-gradient(circle at 45% 40%, rgba(150,180,220,.75), rgba(110,145,200,.55));
  }
  .cover__swoosh { position: absolute; left: 0; bottom: 0; width: 520px; height: 150px; }

  /* content slides */
  .slide__heading {
    position: absolute; left: 20px; top: 20px; white-space: nowrap;
    font-family: "Libre Baskerville", serif; font-weight: 700;
    font-size: 16px; color: var(--ink); text-decoration: underline;
    text-shadow: 1px 1px 2px rgba(0,0,0,.25);
  }
  .slide__band {
    position: absolute; left: 0; bottom: 0; width: 100%; height: 32px;
    background: var(--band);
  }
  .slide__band::before {
    content: ""; position: absolute; left: 0; right: 0; top: -4px; height: 4px;
    background: linear-gradient(90deg, var(--deep), var(--royal));
  }
  .slide__number {
    position: absolute; right: 12px; bottom: 11px;
    font-family: "Carlito", sans-serif; font-size: 9px; color: var(--white);
  }

  .how__tagline {
    position: absolute; left: 0; right: 0; top: 56px; text-align: center;
    font-family: "Tinos", serif; font-weight: 700; font-size: 14px; color: var(--ink);
  }
  .cycle { position: absolute; left: 112px; top: 86px; width: 300px; height: 250px; }
  .cycle__ring { position: absolute; inset: 0; }
  .node {
    position: absolute; width: 96px; height: 40px;
    display: flex; align-items: center; justify-content: center; text-align: center;
    padding: 2px 4px;
    font-family: "Carlito", sans-serif; font-size: 8px; line-height: 1.12; color: var(--white);
    background: linear-gradient(var(--node-top), var(--node-bot));
    border: 1px solid var(--node-edge); border-radius: 6px;
    box-shadow: 1px 2px 3px rgba(0,0,0,.3);
  }

  .agenda__list {
    position: absolute; left: 34px; top: 86px; list-style: none;
  }
  .agenda__item {
    font-weight: 700; font-size: 14px; color: var(--ink);
    margin-bottom: 8px; padding-left: 20px; position: relative; white-space: nowrap;
  }
  .agenda__item::before {
    content: ""; position: absolute; left: 2px; top: 4px;
    border-left: 9px solid var(--ink);
    border-top: 5px solid transparent; border-bottom: 5px solid transparent;
  }
  .agenda__heading { top: 38px; font-size: 20px; }
</style>
</head>
<body>

<section class="slide slide--cover">
  <div class="cover__map" role="img" aria-label="Map of Brazil"></div>
  <h1 class="cover__title">SOCIAL HOUSING IN BRAZIL</h1>
  <div class="cover__rule"></div>
  <p class="cover__subtitle">HIGH YIELD RETURN FOR A QUASI SOVEREIGN RISK</p>
  <svg class="cover__swoosh" viewBox="0 0 520 150" aria-hidden="true">
    <path d="M0 80 Q290 75 520 20 L520 150 L0 150 Z" fill="#1b3f80"/>
    <path d="M0 80 Q290 75 520 20 L520 28 Q290 88 0 90 Z" fill="#c9ccd2"/>
    <path d="M0 90 Q290 88 520 28 L520 34 Q290 96 0 96 Z" fill="#3a3f4a" opacity=".7"/>
  </svg>
  <div class="brand"><span class="brand__dot"></span>RTV</div>
</section>

<section class="slide slide--how">
  <h2 class="slide__heading">HOW TO INVEST IN SOCIAL HOUSING IN BRAZIL?</h2>
  <p class="how__tagline">A socially conscious &amp; lucrative investment</p>
  <div class="cycle">
    <svg class="cycle__ring" viewBox="0 0 300 250" aria-hidden="true">
      <ellipse cx="150" cy="124" rx="102" ry="96" fill="none" stroke="#aebfd8" stroke-width="1.5"/>
    </svg>
    <div class="node" style="left:102px;top:6px">Building housing units for low to middle-class buyers</div>
    <div class="node" style="left:200px;top:52px">Investing in individual projects</div>
    <div class="node" style="left:204px;top:108px">Management Specialized International &amp; local team</div>
    <div class="node" style="left:180px;top:164px">Co-investing with local / mid-size developers</div>
    <div class="node" style="left:102px;top:204px">Co-financed by government</div>
    <div class="node" style="left:2px;top:150px">Equity participation of R$2-10 millions</div>
    <div class="node" style="left:2px;top:94px">Time Horizon 3-4 years</div>
    <div class="node" style="left:22px;top:38px">Target IRR 25-50%</div>
  </div>
  <div class="slide__band"><div class="brand"><span class="brand__dot"></span>RTV</div></div>
  <span class="slide__number">2</span>
</section>

<section class="slide slide--agenda">
  <h2 class="slide__heading agenda__heading">THE TIME IS NOW!</h2>
  <ul class="agenda__list">
    <li class="agenda__item">Macro-environment &amp; Mortgage market: Green Light</li>
    <li class="agenda__item">A sophisticated &amp; successful program: Catalyst</li>
    <li class="agenda__item">Investment Structure of a typical project: Leverage &amp; Limited Risks</li>
    <li class="agenda__item">Small &amp; mid size developers: A partner by choice</li>
    <li class="agenda__item">RTV: Value added &amp; Risk mitigation</li>
    <li class="agenda__item">RTK: RTV, part of an integrated family of companies</li>
    <li class="agenda__item">Appendix: Next step…RTV Fund (2013)</li>
  </ul>
  <div class="slide__band"><div class="brand"><span class="brand__dot"></span>RTV</div></div>
  <span class="slide__number">3</span>
</section>

</body>
</html>
```